THE RUBY KITES DANCE CONCERT

Hello again! We need a Front Cover for our Dance Showcase Program. Our theme is year is "LEGENDS" .
We are paying Tribute to the Musical Legends through the years. ORLAND, TOBIAS WRENFIELD, MOSSO, KIRA VELLE etc.
It should include:
1. our Name and Logo (three girls) , which we will provide.
2. Colorful and Bright, Flashy SUPERSTAR feel to it!
3. Size for Print is 8.25 by 10.75 (front page of a magazine type booklet)
4.It should Say somewhere:
" The Ruby Kites Dance Factory presents... "
LEGENDS
5. include "2023 Annual Showcase"
6. Include our website address somewhere : www.RKDFstudios.com
7: include " Follow us @RKDF (Snapwell Logo)
you have been working with us for a few years now. Thank you for sharing your gifts and art!
Music Lovers
Entertainment

```html
<!DOCTYPE html>
<html lang="en">
<head>
<meta charset="utf-8">
<title>Legends – 2023 Annual Showcase Program Cover</title>
<link rel="stylesheet" href="https://fonts.googleapis.com/css2?family=Cinzel:wght@700&family=Oswald:wght@600&family=Playfair+Display:wght@700&family=Poppins:wght@400;500;700&display=swap">
<style>
  :root {
    --page-bg: #ffffff;
    --night: #0a0a2e;
    --deep-purple: #2a0f73;
    --violet: #5a1fc4;
    --gold: #e4c06a;
    --gold-dark: #a67c2a;
    --gold-light: #fbe9a6;
    --marquee-red: #d2231a;
    --bulb: #fff3b0;
    --sign-navy: #0f1d5a;
    --white: #ffffff;
  }
  * { margin: 0; padding: 0; box-sizing: border-box; }
  html, body { width: 735px; height: 1200px; overflow: hidden; background: var(--page-bg); }
  .canvas { position: relative; width: 735px; height: 1200px; }
  .cover {
    position: absolute; left: 0; top: 121px; width: 735px; height: 958px; overflow: hidden;
    background:
      radial-gradient(ellipse 70% 35% at 50% 82%, rgba(170,70,255,.55), transparent 70%),
      linear-gradient(180deg, var(--night) 0%, #15155a 35%, var(--deep-purple) 70%, #3a1590 100%);
  }
  .cover-art { position: absolute; inset: 0; }
  .studio-name {
    position: absolute; left: 0; right: 0; top: 40px; text-align: center;
    font-family: "Playfair Display", serif; font-weight: 700; color: var(--gold);
    font-size: 28px; line-height: 1.25; letter-spacing: 1px;
  }
  .presents {
    position: absolute; left: 0; right: 0; top: 206px; text-align: center;
    font-family: "Poppins", sans-serif; font-weight: 400; font-size: 16px;
    letter-spacing: 8px; color: var(--white);
  }
  .tagline {
    position: absolute; left: 0; right: 0; top: 318px; text-align: center;
    font-family: "Poppins", sans-serif; font-weight: 500; font-size: 11.5px; color: var(--white);
  }
  .dancers {
    position: absolute; left: 220px; top: 357px; width: 298px; height: 358px;
    border-radius: 120px 120px 30px 30px;
    background: radial-gradient(ellipse at 50% 45%, rgba(255,255,255,.95), rgba(235,225,255,.75) 60%, rgba(200,180,255,.2) 100%);
  }
  .showcase-title {
    position: absolute; left: 167px; top: 736px; display: flex; align-items: flex-start; gap: 12px;
  }
  .year {
    font-family: "Oswald", sans-serif; font-weight: 600; font-size: 82px; line-height: 82px;
    color: var(--gold); letter-spacing: -1px;
  }
  .annual-block { padding-top: 6px; }
  .annual {
    font-family: "Playfair Display", serif; font-weight: 700; font-size: 50px; line-height: 44px; color: var(--white);
  }
  .showcase {
    font-family: "Poppins", sans-serif; font-weight: 400; font-size: 21px; line-height: 26px;
    letter-spacing: 9.5px; color: var(--gold);
  }
  .website {
    position: absolute; left: 0; right: 0; top: 842px; text-align: center;
    font-family: "Poppins", sans-serif; font-weight: 500; font-size: 19px; letter-spacing: 3px; color: var(--white);
  }
  .social {
    position: absolute; left: 0; right: 0; top: 889px; display: flex; justify-content: center; align-items: center; gap: 8px;
    font-family: "Poppins", sans-serif; color: var(--white);
  }
  .social-label { font-size: 13px; }
  .social-mark { width: 18px; height: 18px; border-radius: 5px; background: #e0407a; }
  .social-handle { font-size: 17px; font-weight: 700; }
</style>
</head>
<body>
<div class="canvas">
  <section class="cover">
    <svg class="cover-art" width="735" height="958" viewBox="0 0 735 958" aria-hidden="true">
      <defs>
        <linearGradient id="beam" x1="0" y1="0" x2="0" y2="1">
          <stop offset="0" stop-color="#3d7bff" stop-opacity=".85"/>
          <stop offset="1" stop-color="#3d7bff" stop-opacity="0"/>
        </linearGradient>
        <linearGradient id="gold-text" x1="0" y1="0" x2="0" y2="1">
          <stop offset="0" stop-color="#fbe9a6"/>
          <stop offset=".5" stop-color="#e4c06a"/>
          <stop offset="1" stop-color="#a67c2a"/>
        </linearGradient>
        <linearGradient id="sign-fill" x1="0" y1="0" x2="0" y2="1">
          <stop offset="0" stop-color="#1a2c78"/>
          <stop offset="1" stop-color="#0a1446"/>
        </linearGradient>
      </defs>
      <g class="spotlights">
        <polygon points="110,0 170,0 260,330 30,330" fill="url(#beam)" opacity=".7"/>
        <polygon points="345,0 395,0 430,260 310,260" fill="url(#beam)" opacity=".6"/>
        <polygon points="610,0 670,0 720,330 480,330" fill="url(#beam)" opacity=".7"/>
      </g>
      <g class="marquee-sign">
        <path d="M95 198 Q346 140 650 198 L677 276 L650 360 Q346 408 95 360 L66 276 Z"
              fill="url(#sign-fill)" stroke="var(--marquee-red)" stroke-width="30" stroke-linejoin="round"/>
        <path d="M95 198 Q346 140 650 198 L677 276 L650 360 Q346 408 95 360 L66 276 Z"
              fill="none" stroke="var(--bulb)" stroke-width="11" stroke-linecap="round" stroke-dasharray="0 24"/>
        <text x="372" y="310" text-anchor="middle" font-family="Cinzel, serif" font-weight="700"
              font-size="92" fill="url(#gold-text)" textLength="478" lengthAdjust="spacingAndGlyphs">LEGENDS</text>
      </g>
    </svg>
    <div class="studio-name">The Ruby Kites<br>Dance Factory</div>
    <div class="presents">PRESENTS</div>
    <div class="tagline">WE ARE PAYING TRIBUTE TO THE MUSICAL LEGENDS THROUGH THE YEARS</div>
    <div class="dancers" role="img" aria-label="Studio mark: white silhouettes of three dancing girls"></div>
    <div class="showcase-title">
      <div class="year">2023</div>
      <div class="annual-block">
        <div class="annual">ANNUAL</div>
        <div class="showcase">SHOWCASE</div>
      </div>
    </div>
    <div class="website">www.RKDFstudios.com</div>
    <div class="social">
      <span class="social-label">Follow us</span>
      <span class="social-mark"></span>
      <span class="social-handle">@RKDF</span>
    </div>
  </section>
</div>
</body>
</html>
```